Logo for a gospel Ministry
Logo for a gospel ministry
Project: Logo for a gospel Ministry
Professional
Neema Tuvako & Halida Ruth Sesiwa
Harvesters
P.O Box 27350 Arusha Tanzania
neemahalida42@postmeadow.example

```html
<!DOCTYPE html>
<html lang="en">
<head>
<meta charset="utf-8">
<title>Kindled Hall Ministry – Business Card</title>
<link href="https://fonts.googleapis.com/css2?family=Montserrat:wght@400;500;600;700&display=swap" rel="stylesheet">
<style>
  :root {
    --backdrop: #3b3b3c;
    --card-white: #ffffff;
    --ministry-blue: #1e3c9c;
    --ministry-gold: #b99a3b;
    --ministry-pink: #e6265a;
    --ink: #1e3c9c;
    --ink-soft: #3a4a86;
  }
  * { box-sizing: border-box; margin: 0; padding: 0; }
  html, body {
    width: 1200px;
    height: 804px;
    overflow: hidden;
    background: var(--backdrop);
    font-family: "Montserrat", sans-serif;
  }
  .sheet {
    width: 1200px;
    height: 804px;
    display: flex;
    align-items: center;
    justify-content: center;
    gap: 48px;
  }
  .card {
    width: 540px;
    height: 310px;
    border-radius: 18px;
    position: relative;
    overflow: hidden;
  }
  .card-front {
    background: var(--card-white);
    padding: 34px 36px;
  }
  .card-back {
    background: var(--ministry-blue);
    display: flex;
    align-items: center;
    justify-content: center;
  }
  .brand-name {
    font-weight: 700;
    color: var(--ministry-blue);
    font-size: 22px;
    line-height: 1.1;
    letter-spacing: 0.2px;
  }
  .brand-name-small {
    font-size: 9px;
    font-weight: 700;
    color: var(--ministry-blue);
    letter-spacing: 1.6px;
    text-transform: uppercase;
    margin-top: 3px;
  }
  .holders {
    margin-top: 30px;
    font-size: 17px;
    font-weight: 600;
    color: var(--ink);
    line-height: 1.2;
    max-width: 300px;
  }
  .holders-role {
    margin-top: 4px;
    font-size: 10px;
    font-weight: 500;
    color: var(--ministry-gold);
  }
  .contact-list {
    margin-top: 16px;
    list-style: none;
    font-size: 10px;
    color: var(--ink-soft);
    line-height: 1.7;
  }
  .contact-list li {
    display: flex;
    align-items: center;
    gap: 7px;
  }
  .contact-icon {
    width: 10px;
    height: 10px;
    flex: none;
  }
  .icon-spacer { width: 10px; flex: none; }
  .accent-field {
    position: absolute;
    right: 40px;
    top: 40px;
    width: 150px;
    height: 150px;
    display: flex;
    align-items: center;
    justify-content: center;
  }
  .back-mark {
    display: flex;
    align-items: center;
    gap: 16px;
  }
  .back-mark-dot {
    width: 44px;
    height: 44px;
    border-radius: 50%;
    background: var(--card-white);
    flex: none;
  }
  .back-mark-name {
    font-weight: 700;
    color: var(--card-white);
    font-size: 28px;
    line-height: 1.05;
  }
</style>
</head>
<body>
  <main class="sheet">
    <section class="card card-front" aria-label="Business card front">
      <div class="brand">
        <div class="brand-name">Kindled</div>
        <div class="brand-name-small">Hall Ministry</div>
      </div>
      <div class="holders">Neema Tuvako &amp; Halida Ruth Sesiwa</div>
      <div class="holders-role">Harvesters</div>
      <ul class="contact-list">
        <li>
          <svg class="contact-icon" viewBox="0 0 10 10" aria-hidden="true"><path d="M5 0.5a3.2 3.2 0 0 0-3.2 3.2C1.8 6.2 5 9.5 5 9.5s3.2-3.3 3.2-5.8A3.2 3.2 0 0 0 5 0.5zm0 4.5a1.3 1.3 0 1 1 0-2.6 1.3 1.3 0 0 1 0 2.6z" fill="var(--ministry-blue)"/></svg>
          <span>P.O Box 27350</span>
        </li>
        <li><span class="icon-spacer"></span><span>Arusha Tanzania</span></li>
        <li>
          <svg class="contact-icon" viewBox="0 0 10 10" aria-hidden="true"><path d="M2.2 0.8l1.4 1.9-0.9 1.1c0.6 1.2 1.5 2.1 2.6 2.7l1.1-0.9 1.9 1.3-0.6 1.9C4.4 8.7 1.3 5.6 0.4 1.4z" fill="var(--ministry-blue)"/></svg>
          <span>+255 712 408 336</span>
        </li>
        <li>
          <svg class="contact-icon" viewBox="0 0 10 10" aria-hidden="true"><path d="M2.2 0.8l1.4 1.9-0.9 1.1c0.6 1.2 1.5 2.1 2.6 2.7l1.1-0.9 1.9 1.3-0.6 1.9C4.4 8.7 1.3 5.6 0.4 1.4z" fill="var(--ministry-blue)"/></svg>
          <span>+255 689 150 274</span>
        </li>
        <li>
          <svg class="contact-icon" viewBox="0 0 10 10" aria-hidden="true"><rect x="0.5" y="2" width="9" height="6.4" rx="0.8" fill="none" stroke="var(--ministry-blue)" stroke-width="1"/><path d="M0.8 2.4L5 5.6l4.2-3.2" fill="none" stroke="var(--ministry-blue)" stroke-width="1"/></svg>
          <span>neemahalida42@postmeadow.example</span>
        </li>
      </ul>
      <div class="accent-field" aria-hidden="true"></div>
    </section>

    <section class="card card-back" aria-label="Business card back">
      <div class="back-mark">
        <span class="back-mark-dot" aria-hidden="true"></span>
        <span class="back-mark-name">Kindled Hall<br>Ministry</span>
      </div>
    </section>
  </main>
</body>
</html>
```